i would like a business card to leave with customers and potential customers for electrical work and for the supply and install of reverse cycle airconditioning in the domestic and commercial market.
I own my own business and im a sole trader. I have an a'class electrical lisence and also a refrigeration lisence so i am
able to offer complete installations in airconditioning by a fully qualified and lisenced tradesman.
im looking for something that comes across as unique and professional.
i had the coluor black and some gold in mind but open to any coluors.
something like Beacon Electrical & Refrigeration
or Beacon Air.
i will use this design on a business card to advertise through summer to help generate installs through the busy season.

Target Market(s)

Mainly domestic house holds through summer who are in need of airconditioning and reliable information to acomadate thier cooling and heating requirements

Industry/Entity Type

Electrical

Requirements
Must have
• Business name- Beacon
My name- Peter Wollaston
My mobile no- 0457 819 302
My email- prwollaston@tarvel.com.au
Installation & Decomissioning of aiconditioning split systems
LIC NO: KTR 407516
Nice to have
• Beacon Electrical & Refrigeration

```html
<!DOCTYPE html>
<html lang="en">
<head>
<meta charset="utf-8">
<title>Beacon Electrical &amp; Refrigeration – Business Card</title>
<link href="https://fonts.googleapis.com/css2?family=Arimo:wght@400;700&family=Open+Sans:wght@700&display=swap" rel="stylesheet">
<style>
  :root {
    --gold: #dccb00;
    --gold-soft: #e9df6a;
    --cream: #fbf8e2;
    --ink: #0d0d0d;
    --paper: #ffffff;
    --steel: #8c8c8c;
    --badge-blue: #6bdcfb;
  }
  * { margin: 0; padding: 0; box-sizing: border-box; }
  html, body {
    width: 1200px; height: 1080px; overflow: hidden;
    background: var(--paper);
    font-family: "Arimo", Arial, sans-serif;
  }
  .canvas { position: relative; width: 1200px; height: 1080px; }

  .card {
    position: absolute; top: 70px;
    width: 523px; height: 907px; overflow: hidden;
  }

  /* Front */
  .card--front {
    left: 62px;
    background: linear-gradient(to bottom, var(--gold) 0%, var(--gold-soft) 35%, #f3eca8 60%, var(--cream) 100%);
  }
  .front__band {
    position: absolute; left: 145px; top: 0; width: 240px; height: 270px;
    background: linear-gradient(to bottom, var(--paper) 60%, rgba(255,255,255,0) 100%);
  }
  .front__band::before, .front__band::after {
    content: ""; position: absolute; top: 0; width: 4px; height: 250px;
    background: linear-gradient(to bottom, var(--steel) 70%, rgba(140,140,140,0) 100%);
  }
  .front__band::before { left: -2px; }
  .front__band::after { right: -2px; }

  .brand-mark {
    position: absolute; left: 0; width: 100%; top: 48px;
    display: flex; flex-direction: column; align-items: center; gap: 14px;
  }
  .brand-mark__square { width: 96px; height: 96px; background: var(--ink); }
  .brand-mark__name { font-weight: 700; font-size: 42px; color: var(--ink); line-height: 1; }

  .front__wordmark {
    position: absolute; left: 88px; top: 360px;
    font-weight: 700; font-size: 112px; line-height: 1; color: var(--ink);
  }
  .front__company {
    position: absolute; left: 245px; top: 482px;
    font-family: "Open Sans", Arial, sans-serif; font-weight: 700;
    font-size: 21px; line-height: 1.3; color: var(--ink);
  }
  .contact { position: absolute; left: 0; width: 100%; top: 735px; text-align: center; color: var(--ink); }
  .contact__name { font-weight: 700; font-size: 37px; line-height: 1.1; }
  .contact__phone { font-weight: 700; font-size: 24px; margin-top: 4px; letter-spacing: 0.5px; }
  .contact__email { font-size: 23px; margin-top: 30px; }

  /* Back */
  .card--back { left: 616px; background: var(--ink); }
  .back__service {
    position: absolute; left: 40px; top: 30px;
    color: var(--paper); font-size: 24px; line-height: 1.25; text-align: center;
  }
  .back__badge {
    position: absolute; left: 111px; top: 681px;
    width: 112px; height: 112px; background: var(--badge-blue);
  }
  .back__licence {
    position: absolute; left: 45px; top: 838px;
    color: var(--paper); font-weight: 700; font-size: 22px; letter-spacing: 0.3px;
  }
  .back__wordmark {
    position: absolute; right: -18px; bottom: 30px;
    writing-mode: vertical-rl; transform: rotate(180deg);
    font-weight: 700; font-size: 220px; line-height: 1; color: var(--gold);
  }

  .option-label {
    position: absolute; left: 0; width: 100%; top: 1022px; text-align: center;
    font-weight: 700; font-size: 32px; color: var(--ink);
  }
</style>
</head>
<body>
<main class="canvas">
  <section class="card card--front">
    <div class="front__band"></div>
    <div class="brand-mark">
      <span class="brand-mark__square"></span>
      <span class="brand-mark__name">Beacon</span>
    </div>
    <div class="front__wordmark">Beacon</div>
    <div class="front__company">Beacon Electrical<br>&amp; Refrigeration</div>
    <div class="contact">
      <p class="contact__name">Peter Wollaston</p>
      <p class="contact__phone">0457 819 302</p>
      <p class="contact__email">prwollaston@tarvel.com.au</p>
    </div>
  </section>

  <section class="card card--back">
    <p class="back__service">Installation &amp; Decomissioning<br>of aiconditioning split systems</p>
    <div class="back__badge" role="img" aria-label="Authorised certification badge"></div>
    <p class="back__licence">LIC NO: KTR 407516</p>
    <div class="back__wordmark" aria-hidden="true">Beacon</div>
  </section>

  <p class="option-label">Option 2</p>
</main>
</body>
</html>
```